Flyer-Design
Sehr flexibel bei Änderungswünschen. Herzlichen Dank. Würde jederzeit wieder mit Bettina zusammenarbeiten.
Zielgruppe
Wir sind eine eine Praxis und unsere Zielgruppe sind Kunden. Es sollte einen Faltflyer geben, welcher Doppelseitig bedruckt wird.
Aufgabenstellung
Ich habe genaue Vorstellungen, wie dieser Flyer aussehen soll. Jedoch bin ich auch auf neue Ideen gespannt :). Wunschvorstellung wäre ein Falzflyer (siehe Bild Musterfyler). Des weiteren habe ich ein Word gemacht, mit dem gesamten Inhalt des Textes und wie der Flyer am Besten aufgebaut werden sollte. (siehe Flyer Tierversicherung).
Die beiden letzten Abschnitte (Tipp an unsere Kunden, Fazit) sollten ein wenig auffallen. Müssen auch nicht am Schluss sein.
Des weiteren wäre ich dankbar, wenn das CI/CD der Unternehmung berücksichtig wird. Bitte werfen Sie einen Blick auf die Webseite www.felgor-tieraerzte.ch. Ein Logo ist ebenfalls im Anhang. Bei Fragen bitte melden.
Ich freue mich auf Vorschläge.

```html
<!DOCTYPE html>
<html lang="de">
<head>
<meta charset="utf-8">
<title>Faltflyer Tierversicherungen – Felgor Tierärzte</title>
<link href="https://fonts.googleapis.com/css2?family=Arimo:wght@400;700&display=swap" rel="stylesheet">
<style>
:root{
  --wine-dark:#4a0812;
  --wine:#7a0f22;
  --red:#a8142c;
  --pink:#c8164b;
  --paper:#ffffff;
  --bg:#eeeeee;
  --text-light:#f6e9ec;
}
*{box-sizing:border-box;margin:0;padding:0}
html,body{width:1200px;height:2970px;overflow:hidden}
body{background:var(--bg);font-family:"Arimo",Arial,sans-serif;color:var(--text-light);position:relative}
.spread{position:absolute;left:45px;width:1110px;height:785px;display:flex;box-shadow:0 10px 30px rgba(0,0,0,.25)}
.spread--outside{top:520px}
.spread--inside{top:1560px}
.panel{position:relative;width:370px;height:785px;overflow:hidden}
.photo{position:absolute;left:0;top:0;width:100%}
.photo--cat{height:420px;background:linear-gradient(160deg,#e4e1dc 0%,#b3a898 40%,#7d746a 70%,#4a4644 100%)}
.photo--dog{height:520px;background:linear-gradient(180deg,#f1efec 0%,#d8c7b6 35%,#c4384c 70%,#b3182f 100%)}

/* intro panel */
.panel--intro{background:linear-gradient(180deg,var(--red) 420px,var(--wine) 620px,var(--wine-dark) 785px)}
.intro-text{position:absolute;left:22px;right:22px;top:440px;font-size:12px;line-height:1.3;text-align:justify}
.intro-text p{margin-bottom:8px}

/* contact panel */
.panel--contact{background:linear-gradient(180deg,var(--wine-dark),var(--wine) 50%,var(--wine-dark))}
.contact-block{position:absolute;left:22px;right:14px;font-size:13px;line-height:1.55}
.contact-block h2{font-weight:400;font-size:25px;margin-bottom:8px;color:#fff}
.hours{top:385px}
.hours dl{display:grid;grid-template-columns:84px 1fr}
.hours dd{margin:0}
.hours p{margin-top:8px}
.contact{top:590px}
.contact p{font-weight:700}

/* cover panel */
.panel--cover{background:linear-gradient(180deg,var(--red) 520px,var(--wine) 680px,var(--wine-dark) 785px)}
.cover-title{position:absolute;left:14px;right:10px;top:545px;text-align:center;color:#fff;font-size:22px;font-weight:400;line-height:1.25}
.cover-title strong{display:block;font-size:32px;font-weight:400;margin-top:6px}
.brand-band{position:absolute;left:0;right:0;top:680px;height:78px;background:var(--paper);display:flex;align-items:center;justify-content:center}
.brand{font-size:22px;font-weight:400;color:var(--red);letter-spacing:2px;text-transform:uppercase}

/* inside glossary */
.panel--glossary{background:linear-gradient(180deg,var(--wine-dark),var(--wine) 55%,var(--red))}
.panel--mid{background:linear-gradient(180deg,var(--wine-dark),var(--wine) 60%,var(--red))}
.glossary{position:absolute;left:22px;right:22px;top:16px;font-size:12px;line-height:1.3;text-align:justify}
.letter{font-size:14px;border-bottom:1px solid rgba(255,255,255,.55);padding-bottom:1px;margin:8px 0 4px}
.letter:first-child{margin-top:0}
.term{font-weight:700;margin-top:4px}
.glossary p{margin-bottom:4px}
.lead{font-size:14px;line-height:1.25}
.tip-box{position:absolute;left:0;right:0;top:570px;bottom:0;background:var(--pink);padding:14px 22px;font-size:11.5px;line-height:1.3;text-align:justify}
.tip-box h3{font-size:13px;font-weight:400;display:flex;align-items:center;gap:6px;margin-bottom:8px}
.tip-box h4{font-size:12px;font-weight:700;margin-top:7px}
</style>
</head>
<body>

<section class="spread spread--outside" aria-label="Aussenseite">
  <article class="panel panel--intro">
    <div class="photo photo--cat" role="img" aria-label="Foto einer Katze mit Schutzkragen"></div>
    <div class="intro-text">
      <p>Haustiere sind für viele von uns von grosser Bedeutung und sensible Weggefährten, mit denen sich lachen, reden und auch einmal weinen lässt. Neben den vielen Vorzügen, die ein eigenes Haustier mit sich bringen, können diese auch krank werden oder einen Unfall haben.</p>
      <p>Wenn eine Behandlung das geliebte Haustier retten kann, jedoch hohe Kosten für Medikamente, Behandlungen, Operationen oder Klinikaufenthalte auslöst, dann entstehen bei vielen Personen ernsthafte Sorgen und Belastungen, denen allerdings vorgebeugt werden kann.</p>
      <p>Mit einem Abschluss einer Tierversicherung gegen Unfall und Krankheit können verschiedene Vorkehrungen getroffen werden, um hohe Kosten im Ernstfall zu reduzieren.</p>
      <p>Daher ist es wichtig, dass man sich vorgängig über die Möglichkeiten einer Tierversicherung gegen Unfall und Krankheit informiert, um bestmöglich vorbereitet zu sein, sollte es dem treuen Begleiter einmal schlecht gehen.</p>
      <p>In diesem Flyer finden Sie alles von A-Z, was sie über Tierversicherungen gegen Unfall und Krankheit wissen müssen.</p>
    </div>
  </article>

  <article class="panel panel--contact">
    <div class="contact-block hours">
      <h2>Öffnungszeiten</h2>
      <dl>
        <dt>Mo bis Fr:</dt><dd>8.00 – 12.00 und<br>13.30 - 18.00 Uhr</dd>
        <dt>Sa:</dt><dd>8.00 – 12.00 Uhr</dd>
      </dl>
      <p>Dringende Notfälle auch ausserhalb<br>der Kliniköffnungszeiten.</p>
    </div>
    <div class="contact-block contact">
      <h2>Kontakt</h2>
      <p>Felgor Tierärzte | Kleintierpraxis / Grosstierpraxis<br>Lindenweg 8 | 6410 Seewil<br>Tel.: 041 555 01 23<br>Web: http://www.felgor-tieraerzte.ch</p>
    </div>
  </article>

  <article class="panel panel--cover">
    <div class="photo photo--dog" role="img" aria-label="Foto eines kleinen Hundes mit rotem Strickschal"></div>
    <h1 class="cover-title">Tierversicherungen gegen Unfall und Krankheit:<strong>Fluch oder Segen?</strong></h1>
    <div class="brand-band"><span class="brand">Felgor Tierärzte</span></div>
  </article>
</section>

<section class="spread spread--inside" aria-label="Innenseite">
  <article class="panel panel--glossary">
    <div class="glossary">
      <div class="letter">A</div>
      <div class="term">Abschluss</div>
      <p class="lead">Beim Abschluss einer Versicherung muss das Tier jung und gesund sein.</p>
      <div class="term">Anbieter</div>
      <p>Auf dem Schweizer Markt gibt verschiedene Anbieter von Tierversicherungen wie beispielsweise Tierovia, Pfotenglück, Equila, Domisana, Alpensure und Vitalis.</p>
      <p>Wir empfehlen keinen konkreten Anbieter, da es viele verschiedene unterschiedliche Produkte auf dem Markt gibt und jeder Kunde andere Wünsche und ein anderes Budget hat. Unseres Erachtens liegen die Unterschiede im Detail.</p>
      <div class="term">Altersbegrenzung</div>
      <p>Die Anbieter von Tierversicherungen haben Altersbegrenzungen, üblicherweise betragen diese fünf Jahre bei Katzen und sechs Jahre bei Hunden.</p>
      <div class="term">Arztwahl</div>
      <p>Gewisse Versicherungen erlauben keine freie Tierarztwahl. Sichern Sie sich bei Vertragsabschluss ab und fragen, sie explizit nach.</p>
      <div class="term">Aufnahmealter</div>
      <p>Die Versicherungsanbieter nehmen die Tiere in der Regel im Alter von 3 Monaten auf. Wir empfehlen die Tiere so früh wie möglich zu versichern.</p>
      <div class="term">Ausschlüsse</div>
      <p>Beachten sie, ob Ausschlüsse aus einer Versicherungsleistung existieren und ob diese für sie von Bedeutung sind.</p>
      <div class="letter">G</div>
      <div class="term">Geburtskrankheiten/Erbkrankheiten</div>
      <p>Diese werden bei vielen Angeboten ausgeschlossen oder müssen explizit dazu versichert werden.</p>
      <div class="letter">I</div>
      <div class="term">Impfungen</div>
      <p>Nur wenige Anbieter übernehmen auch Impfungen. Fall ein Anbieter diese Leistung übernimmt, hat er in der Regel einen maximalen Betrag festgelegt.</p>
      <div class="letter">K</div>
      <div class="term">Karenzfrist</div>
      <p>Bei Versicherungen besteht jeweils eine Wartezeit, die</p>
    </div>
  </article>

  <article class="panel panel--mid">
    <div class="glossary">
      <p>zwischen Unterzeichnung der Police und einem Deckungsanspruch eingehalten werden muss. In der Regel beträgt diese für nicht-chronische Krankheiten einen Monat und bei chronischen Krankheiten drei Monate. Bei einem Unfall gibt es in der Regel keine Karenzfrist oder je nach Anbieter bis zu einem Monat.</p>
      <div class="letter">L</div>
      <div class="term">Leistungen</div>
      <p>Die inkludierten Leistungen und die gebotene Abdeckung ist genau zu prüfen. Übernimmt der Versicherungsanbieter alle Behandlungen oder sind zum Beispiel chronische Krankheiten oder Erbkrankheiten ausgeschlossen. Ein Blick auf das Kleingedruckte beim Versicherungsangebot lohnt sich.</p>
      <p>Sie können ihr Tier entweder gegen Krankheit oder gegen Unfall oder gegen beides versichern, letzteres empfehlen wir Ihnen.</p>
      <div class="letter">P</div>
      <div class="term">Prämien</div>
      <p>Die Prämien der einzelnen Anbieter fallen unterschiedlich aus, deshalb ist es wichtig Versicherungsangebote zu vergleichen, um den passenden Tarif für ihr Haustier zu finden.</p>
      <div class="term">Prämienerhöhung</div>
      <p>Es gibt Versicherungen, die während der Laufzeit die Prämien erhöhen, andere bieten einen Pauschalbetrag an, damit Planungssicherheit geboten wird.</p>
    </div>
    <aside class="tip-box">
      <h3><svg width="15" height="15" viewBox="0 0 14 14" aria-hidden="true"><circle cx="7" cy="7" r="6" fill="none" stroke="#fff" stroke-width="1.2"/><rect x="6.3" y="6" width="1.4" height="4.5" fill="#fff"/><circle cx="7" cy="4" r=".9" fill="#fff"/></svg>Tipp an unsere Kunden</h3>
      <p>Wir empfehlen Ihnen die die Tierarztkosten der letzten Jahre zusammenzustellen und zu prüfen, ob sie von der gewählten Versicherung übernommen worden wären. Bei diesem Vergleich darf aber der Selbstbehalt nicht ausser Acht gelassen werden.</p>
      <h4>Fazit</h4>
      <p>Wir von der Felgor Tierärzte AG haben bisher sehr gute Erfahrungen mit Tierversicherungen unserer Kunden gemacht. Wir empfehlen Ihnen jedoch etwas Zeit in die Auswahl einer für sie passenden Tierversicherung zu investieren.</p>
    </aside>
  </article>

  <article class="panel panel--glossary">
    <div class="glossary">
      <div class="term">Preis</div>
      <p>Langfristig ist billigste Vertragsoption oft nicht die beste, da einige Versicherungen mit einem günstigeren Preis starten und im Laufe der Jahre, wenn das Tier älter wird, den Tarif erhöht.</p>
      <div class="letter">R</div>
      <div class="term">Rabatte</div>
      <p>Vereinzelte Versicherungsanbieter gewähren Rabatte, wenn in einem Versicherungsjahr keine Leistungen bezogen wurden.</p>
      <div class="term">Rechnungsstellung</div>
      <p>Die erbrachten Leistungen durch den Tierarzt sind direkt vom Tierhalter zu bezahlen. Anschliessend kann die Rechnung beim Versicherungsanbieter eingereicht werden.</p>
      <div class="letter">S</div>
      <div class="term">Schadenfall</div>
      <p>Wenn ein Schadensfall eintritt, direkt den Tierarzt aufsuchen und erst anschliessend den Fall bei der Versicherung melden und gleich die Kostenübernahme abklären. Die Rechnungskopie wird bei Behandlungsabschluss der Versicherung zu Prüfung und Begleichung weitergeleitet.</p>
      <div class="term">Selbstbehalt</div>
      <p>Der Selbstbehalt gibt an, welche Kosten bei einem Versicherungsfall selbst zu tragen sind. Einige Anbieter bieten ebenfalls die Option mit CHF 0 an. Falls man bei der Prämie etwas sparen möchte, sollte der Selbstbehalt auf einen höheren Betrag festgelegt werden. Einige Versicherungsanbieter ziehen den Selbstbehalt bei jedem Krankheitsfall an und andere jährlich.</p>
      <div class="letter">V</div>
      <div class="term">Versicherungsende</div>
      <p>Das Haustier ist solange versichert, wie der Halter die Prämien bezahlt und das Tier lebt.</p>
      <div class="term">Versicherungssumme</div>
      <p>Dies ist der Höchstbetrag, den der Kunden von einem Versicherungsanbieter für eine Behandlung eines Haustieres erhält.</p>
      <div class="term">Vertragsdauer</div>
      <p>Die Mindestlaufzeit von Tierversicherungen beträgt in der Regel ein Jahr.</p>
    </div>
  </article>
</section>

</body>
</html>
```